Business card design needed for a security services business.

We provide a wide range of security services from guard personnel to electronic systems.

Industry/Entity Type

Security Industry

Contact Information for Business Card

Brent Holloway, Owner Office: 780.555.0148; Cell: 780.555.0193 Email: brent@norcrestwatchgroup.example; Address 20487 163 St Edmonton, AB T5X 2K8

Colors
0054AA
0677BA
7BADD7
CADEEF
E8F1F8

Requirements
Nice to have
• On the back of the card I would like to possible list the services I provide: Guards Mobiles Live Video Surveillance Access Intrusion

```html
<!DOCTYPE html>
<html lang="en">
<head>
<meta charset="utf-8">
<title>Norcrest Watch Group – Business Card</title>
<link rel="stylesheet" href="https://fonts.googleapis.com/css2?family=Montserrat:wght@400;500;700&display=swap">
<style>
  :root {
    --backdrop: #d9d9d7;
    --card-white: #ffffff;
    --card-grey: #666666;
    --brand-blue: #0677ba;
    --deep-blue: #0054aa;
    --text-grey: #555555;
    --mark-grey: #4b4b4d;
    --rule-grey: #6d6d6d;
  }
  * { box-sizing: border-box; margin: 0; padding: 0; }
  html, body {
    width: 1200px; height: 801px; overflow: hidden;
    background: var(--backdrop);
    font-family: "Montserrat", sans-serif;
  }
  .sheet {
    width: 1200px; height: 801px;
    display: flex; align-items: center; justify-content: center; gap: 60px;
  }
  .card {
    width: 525px; height: 300px; position: relative;
    border-bottom: 4px solid var(--brand-blue);
    box-shadow: 0 10px 24px rgba(0,0,0,.18);
  }
  .card--front { background: var(--card-white); }
  .card--back { background: var(--card-grey); display: flex; align-items: center; justify-content: center; }

  .brand {
    position: absolute; left: 34px; top: 112px; width: 200px;
    display: flex; align-items: center; gap: 10px;
  }
  .brand__square { width: 16px; height: 16px; background: var(--brand-blue); flex: none; }
  .brand__name {
    color: var(--brand-blue); font-weight: 700; font-size: 19px; line-height: 1.15;
    text-transform: uppercase; letter-spacing: .5px;
  }
  .brand-rule {
    position: absolute; left: 34px; top: 176px; width: 200px; height: 2px;
    background: var(--rule-grey);
  }

  .divider {
    position: absolute; left: 252px; top: 40px; width: 1px; height: 152px;
    background: var(--brand-blue);
  }
  .contact { position: absolute; left: 272px; top: 36px; color: var(--text-grey); }
  .contact__name {
    color: var(--brand-blue); font-weight: 700; font-size: 20px;
    text-transform: uppercase; letter-spacing: .5px;
  }
  .contact__role { font-size: 13px; margin-bottom: 6px; }
  .contact__address { font-size: 11.5px; line-height: 1.35; margin-bottom: 8px; }
  .contact__list { list-style: none; font-size: 11.5px; line-height: 1.6; }
  .contact__list li { display: flex; align-items: center; gap: 7px; }
  .contact__list svg { width: 10px; height: 10px; flex: none; }

  .services {
    position: absolute; left: 34px; right: 24px; bottom: 26px;
    display: flex; gap: 18px; list-style: none;
    color: var(--brand-blue); font-size: 12.5px; font-weight: 500;
  }
  .services li::before { content: "•"; margin-right: 4px; }

  .back__name {
    color: var(--mark-grey); font-weight: 700; font-size: 34px;
    text-transform: uppercase; letter-spacing: 2px; text-align: center; line-height: 1.15;
  }
</style>
</head>
<body>
<main class="sheet">
  <section class="card card--front">
    <div class="brand">
      <span class="brand__square"></span>
      <span class="brand__name">Norcrest<br>Watch Group</span>
    </div>
    <div class="brand-rule"></div>

    <div class="divider"></div>

    <div class="contact">
      <h1 class="contact__name">Brent Holloway</h1>
      <p class="contact__role">Owner</p>
      <p class="contact__address">20487 163 St Edmonton<br>AB T5X 2K8</p>
      <ul class="contact__list">
        <li>
          <svg viewBox="0 0 10 10" aria-hidden="true"><path d="M2 1l2 2-1 1.2c.6 1.2 1.6 2.2 2.8 2.8L7 6l2 2-1.2 1.5C4.5 9.2.8 5.5.5 2.2z" fill="var(--deep-blue)"/></svg>
          780.555.0148
        </li>
        <li>
          <svg viewBox="0 0 10 10" aria-hidden="true"><rect x="2.5" y=".8" width="5" height="8.4" rx="1" fill="none" stroke="var(--deep-blue)" stroke-width="1.1"/></svg>
          780.555.0193
        </li>
        <li>
          <svg viewBox="0 0 10 10" aria-hidden="true"><rect x=".5" y="2" width="9" height="6.5" fill="var(--deep-blue)"/><path d="M.8 2.3L5 5.6l4.2-3.3" fill="none" stroke="#fff" stroke-width=".9"/></svg>
          brent@norcrestwatchgroup.example
        </li>
        <li>
          <svg viewBox="0 0 10 10" aria-hidden="true"><circle cx="5" cy="5" r="4.3" fill="none" stroke="var(--deep-blue)" stroke-width="1.1"/><path d="M.8 5h8.4M5 .7c-2.4 2.6-2.4 6 0 8.6M5 .7c2.4 2.6 2.4 6 0 8.6" fill="none" stroke="var(--deep-blue)" stroke-width=".8"/></svg>
          www.norcrestwatchgroup.example
        </li>
      </ul>
    </div>

    <ul class="services">
      <li>Guards Mobiles Live</li>
      <li>Video Surveillance</li>
      <li>Access Intrusion</li>
    </ul>
  </section>

  <section class="card card--back">
    <p class="back__name">Norcrest<br>Watch Group</p>
  </section>
</main>
</body>
</html>
```